Banner 34"x81"

This is for a Pull Up Banner
I am supplying a sample of my logo and some of my art work for you to incorporate into an upright banner.
Please business name:TessaLo QuietHarbor Psychotherapy
phone number: 905-318-4470 NOT THE ONE ON THE BUSINESS CARD

```html
<!DOCTYPE html>
<html lang="en">
<head>
<meta charset="utf-8">
<title>TessaLo QuietHarbor Psychotherapy – Pull Up Banner</title>
<link rel="stylesheet" href="https://fonts.googleapis.com/css2?family=Open+Sans:wght@400;700&family=Oswald:wght@300&family=Lexend:wght@600&family=Noto+Sans+TC:wght@300&display=swap">
<style>
  :root {
    --night: #0b0f1a;
    --sparkle-dark: #0a0805;
    --sparkle-gold: #b8902c;
    --sparkle-light: #e8c866;
    --white: #ffffff;
    --accent-red: #d0222a;
    --sky-blue: #3ca8e0;
    --brand-blue: #2259a8;
    --phone-yellow: #f4e063;
    --photo-blue: #2f66c4;
    --photo-brown: #3a1f1c;
  }
  * { margin: 0; padding: 0; box-sizing: border-box; }
  html, body { width: 1200px; height: 2859px; overflow: hidden; background: var(--sparkle-dark); }
  .banner { position: relative; width: 1200px; height: 2859px; overflow: hidden; font-family: "Open Sans", sans-serif; color: var(--white); }
  .sparkle-backdrop {
    position: absolute; inset: 0;
    background:
      radial-gradient(ellipse at 50% 100%, var(--sparkle-light) 0%, var(--sparkle-gold) 25%, transparent 55%),
      radial-gradient(ellipse at 20% 10%, rgba(184,144,44,0.35) 0%, transparent 40%),
      radial-gradient(ellipse at 85% 30%, rgba(184,144,44,0.3) 0%, transparent 40%),
      var(--sparkle-dark);
  }
  .panel { position: absolute; left: 110px; top: 209px; width: 982px; height: 2375px; background: var(--night); }
  .frame { position: absolute; left: 202px; top: 274px; width: 792px; height: 1427px; border: 3px solid var(--white); }
  .accent-arrows { position: absolute; left: 158px; top: 531px; }
  .portrait {
    position: absolute; left: 331px; top: 150px; width: 532px; height: 532px; border-radius: 50%;
    background: linear-gradient(180deg, var(--photo-brown) 0%, #4a2b26 55%, var(--photo-blue) 80%, var(--photo-blue) 100%);
  }
  .name { position: absolute; left: 0; width: 1200px; top: 752px; text-align: center; font-weight: 700; font-size: 116px; line-height: 1; letter-spacing: -1px; }
  .brand-cn {
    position: absolute; left: 305px; top: 949px; width: 152px; height: 638px;
    writing-mode: vertical-rl; font-family: "Noto Sans TC", sans-serif; font-weight: 300;
    font-size: 150px; line-height: 152px; color: var(--sky-blue); text-align: center; letter-spacing: 14px;
  }
  .brand-square { position: absolute; left: 535px; top: 1273px; width: 371px; height: 302px; background: var(--brand-blue); }
  .practice-name {
    position: absolute; left: 0; width: 1200px; top: 1742px; text-align: center;
    font-family: "Oswald", sans-serif; font-weight: 300; font-size: 176px; line-height: 1; letter-spacing: 4px; text-transform: uppercase;
  }
  .practice-type { position: absolute; left: 0; width: 1200px; top: 1940px; text-align: center; font-weight: 700; font-size: 96px; line-height: 1.1; }
  .phone { position: absolute; left: 0; width: 1200px; top: 2152px; text-align: center; font-family: "Lexend", sans-serif; font-weight: 600; font-size: 86px; line-height: 1; color: var(--phone-yellow); letter-spacing: 2px; }
  .email { position: absolute; left: 0; width: 1200px; top: 2252px; text-align: center; font-size: 50px; line-height: 1.1; }
  .social { position: absolute; top: 2369px; width: 460px; text-align: center; }
  .social.left { left: 174px; }
  .social.right { left: 654px; }
  .social-dot { display: block; width: 68px; height: 68px; margin: 0 auto 10px; border-radius: 50%; background: var(--phone-yellow); }
  .social-handle { font-size: 38px; line-height: 1.1; }
</style>
</head>
<body>
<div class="banner">
  <div class="sparkle-backdrop" role="img" aria-label="Dark background with falling gold glitter sparkles, denser gold glitter along the bottom"></div>
  <div class="panel"></div>
  <div class="frame"></div>
  <svg class="accent-arrows" width="93" height="168" viewBox="0 0 93 168" aria-hidden="true">
    <polygon points="46.5,0 93,69 0,69" fill="var(--accent-red)"/>
    <polygon points="46.5,100 93,168 0,168" fill="var(--accent-red)"/>
  </svg>
  <div class="portrait" role="img" aria-label="Portrait photo of the therapist seated in a brown leather chair, wearing a blue sweater"></div>
  <div class="name">TessaLo</div>
  <div class="brand-cn" lang="zh-Hant">靜港</div>
  <div class="brand-square"></div>
  <div class="practice-name">Quiet Harbor</div>
  <div class="practice-type">Psychotherapy</div>
  <div class="phone">905-318-4470</div>
  <div class="email">TessaQuietHarbor@mailbox.com</div>
  <div class="social left"><span class="social-dot"></span><span class="social-handle">@TessaQuietHarbour</span></div>
  <div class="social right"><span class="social-dot"></span><span class="social-handle">@TessaHarbor</span></div>
</div>
</body>
</html>
```